I need some Graphic Design for Planning Poker Cards (AI, PSD, EPS, PDF, PNG)

Hi Designers,

======= PLEASE SEE THE ATTACHMENTS ALSO ========

I would like to design the graphics for Planning Poker cards which are used for Planning Estimation in SCRUM.
You can easily find how the real cards look like by searching it in Google.

I would like to receive the final handover files in these formats: AI, EPS, PSD, PDF, PNG. (Is it Corel Draw format possible?)
And also I want all the Font files which were used in the design.

PLEASE SEE THE ATTACHMENTS FOR:
- Details Requirements - including many samples inside
- Example I found in the internet
- Designed files for Logo of my company (LKMORA)

Thanks,
Khiem.

```html
<!DOCTYPE html>
<html lang="en">
<head>
<meta charset="utf-8">
<title>LKMORA Planning Poker Cards</title>
<link rel="stylesheet" href="https://fonts.googleapis.com/css2?family=Open+Sans:wght@400;600&display=swap">
<style>
  :root {
    --card-red: #be1e2d;
    --frame-navy: #1e2240;
    --ink-white: #ffffff;
    --ink-navy: #16203a;
    --page: #ffffff;
  }
  * { box-sizing: border-box; margin: 0; padding: 0; }
  html, body { width: 1200px; height: 844px; overflow: hidden; background: var(--page); }
  body { position: relative; font-family: "Open Sans", Arial, sans-serif; color: var(--ink-white); }

  .card {
    position: absolute;
    width: 270px;
    height: 376px;
    background: var(--card-red);
    border-radius: 16px;
    overflow: hidden;
  }
  .card::before {
    content: "";
    position: absolute;
    inset: 12px 10px 10px 14px;
    border: 2px solid var(--frame-navy);
    border-radius: 14px;
  }
  .row-top { top: 19px; }
  .row-bottom { top: 424px; height: 384px; }
  .col-1 { left: 16px; }
  .col-2 { left: 307px; }
  .col-3 { left: 603px; }
  .col-4 { left: 897px; }

  .brand-dot {
    position: absolute;
    top: 16px; right: 20px;
    width: 34px; height: 34px;
    border: 3px solid var(--ink-white);
    border-radius: 50%;
  }
  .index {
    position: absolute;
    font-size: 32px;
    line-height: 1;
    font-weight: 400;
  }
  .index-top { top: 24px; left: 26px; }
  .index-bottom { bottom: 22px; right: 26px; transform: rotate(180deg); }
  .index-small { font-size: 22px; }
  .index-wide { font-size: 46px; }
  .index-flip { transform: none; }

  .face {
    position: absolute;
    inset: 0;
    display: flex;
    align-items: center;
    justify-content: center;
  }
  .face-value { font-size: 250px; font-weight: 400; line-height: 1; }
  .face-infinity { font-size: 250px; line-height: 1; }
  .face-question { font-size: 220px; line-height: 1; }

  .shirt {
    background: var(--ink-white);
    color: var(--ink-navy);
    display: flex;
    align-items: center;
    justify-content: center;
    border-radius: 22px 22px 10px 10px;
  }
  .shirt-xs { width: 124px; height: 136px; font-size: 40px; margin-top: 30px; }
  .shirt-xxl { width: 230px; height: 250px; font-size: 50px; margin-top: 20px; }
  .shirt-open { width: 230px; height: 250px; font-size: 150px; font-weight: 600; margin-top: 20px; }

  .cup-art {
    width: 140px; height: 150px;
    background: var(--ink-white);
    border-radius: 10px 10px 40px 40px;
    margin-top: 30px;
  }
  .cup-icon { position: absolute; width: 40px; height: 34px; }
  .cup-icon-top { top: 22px; left: 22px; }
  .cup-icon-bottom { bottom: 20px; right: 22px; transform: rotate(180deg); }

  .back-lockup {
    position: absolute;
    left: 30px; top: 240px;
    transform-origin: 24px 24px;
    transform: rotate(-55deg);
    white-space: nowrap;
    display: flex;
    align-items: flex-start;
    gap: 8px;
  }
  .back-mark {
    flex: none;
    width: 48px; height: 48px;
    border: 4px solid var(--ink-white);
    border-radius: 50%;
  }
  .back-words { display: flex; flex-direction: column; }
  .back-name { font-size: 46px; font-weight: 600; line-height: 0.9; letter-spacing: 1px; }
  .back-tagline { font-size: 8px; letter-spacing: 0.5px; margin-top: 3px; }
  .back-company { font-size: 16px; letter-spacing: 0.5px; margin-top: 2px; }
</style>
</head>
<body>

  <div class="card card-back row-top col-1">
    <div class="back-lockup">
      <div class="back-mark"></div>
      <div class="back-words">
        <span class="back-name">LKMORA</span>
        <span class="back-tagline">ESTIMATE WITH CONFIDENCE</span>
        <span class="back-company">LKMORA CREATIVE STUDIO</span>
      </div>
    </div>
  </div>

  <div class="card row-top col-2">
    <span class="brand-dot"></span>
    <span class="index index-top">0</span>
    <div class="face"><span class="face-value">0</span></div>
    <span class="index index-bottom">0</span>
  </div>

  <div class="card row-top col-3">
    <span class="brand-dot"></span>
    <span class="index index-top index-wide">∞</span>
    <div class="face"><span class="face-infinity">∞</span></div>
    <span class="index index-bottom index-wide">∞</span>
  </div>

  <div class="card row-top col-4">
    <span class="brand-dot"></span>
    <span class="index index-top">?</span>
    <div class="face"><span class="face-question">?</span></div>
    <span class="index index-bottom index-flip">¿</span>
  </div>

  <div class="card row-bottom col-1">
    <span class="brand-dot"></span>
    <span class="index index-top index-small">XS</span>
    <div class="face"><div class="shirt shirt-xs" role="img" aria-label="T-shirt illustration marked XS">XS</div></div>
    <span class="index index-bottom index-small">XS</span>
  </div>

  <div class="card row-bottom col-2">
    <span class="brand-dot"></span>
    <span class="index index-top index-small">XXL</span>
    <div class="face"><div class="shirt shirt-xxl" role="img" aria-label="T-shirt illustration marked XXL">XXL</div></div>
    <span class="index index-bottom index-small">XXL</span>
  </div>

  <div class="card row-bottom col-3">
    <span class="brand-dot"></span>
    <span class="index index-top">?</span>
    <div class="face"><div class="shirt shirt-open" role="img" aria-label="T-shirt illustration with a question mark">?</div></div>
    <span class="index index-bottom index-flip">¿</span>
  </div>

  <div class="card row-bottom col-4">
    <span class="brand-dot"></span>
    <svg class="cup-icon cup-icon-top" viewBox="0 0 40 34" aria-hidden="true">
      <path d="M4 14 h26 v8 a9 9 0 0 1 -9 9 h-8 a9 9 0 0 1 -9 -9z" fill="#fff"/>
      <path d="M30 16 a5 5 0 0 1 0 10" stroke="#fff" stroke-width="2.5" fill="none"/>
      <path d="M11 10 q-3 -4 0 -8 M17 10 q-3 -4 0 -8 M23 10 q-3 -4 0 -8" stroke="#fff" stroke-width="2" fill="none"/>
    </svg>
    <div class="face"><div class="cup-art" role="img" aria-label="Steaming coffee cup illustration for a break"></div></div>
    <svg class="cup-icon cup-icon-bottom" viewBox="0 0 40 34" aria-hidden="true">
      <path d="M4 14 h26 v8 a9 9 0 0 1 -9 9 h-8 a9 9 0 0 1 -9 -9z" fill="#fff"/>
      <path d="M30 16 a5 5 0 0 1 0 10" stroke="#fff" stroke-width="2.5" fill="none"/>
      <path d="M11 10 q-3 -4 0 -8 M17 10 q-3 -4 0 -8 M23 10 q-3 -4 0 -8" stroke="#fff" stroke-width="2" fill="none"/>
    </svg>
  </div>

</body>
</html>
```